Van Sign Writing for Electrical & Security Systems Compay

We are an Electrical, Intruder Alarm / CCTV and Automation company. We would like a design to have our van Sign Written. The van is a 2021 Velmont corvane. We DON'T want to completely wrap it, just work with the colour of the van and the logo and wording provided. Although we are open to some unique designs to complement the logo and wording. Pictures of the van front, side and back have been provided along with the logo.

Please use fake placeholders for the Phone Number Email Address and Web Address, these will be provided later.

The Servies that need to be displayed are:

Electrical
Intruder Alarms & CCTV
Access Control
EV Chargers
Home Automation
Fire Alarms
Fire Protection

The social media Icons that need to be displayed are:
Lunemark
Quellorix
Bravitel
Marquine
Dovlette
There needs to be space under these icons for a web address. The exact van colour is VELMONT PAINT KPW GRIS URBAN. The image also attached of colour.

Target Market(s)

Electrical
Intruder Alarms & CCTV
Access Control
EV Chargers
Home Automation
Fire Alarms
Fire Protection

Requirements
Must have
• As per Description
Nice to have
• Unique design to compliment text, logo and colours
Should not have
• Full wrap

```html
<!DOCTYPE html>
<html lang="en">
<head>
<meta charset="utf-8">
<title>Kynetra Van Side Sign Writing</title>
<link rel="stylesheet" href="https://fonts.googleapis.com/css2?family=Poppins:ital,wght@0,600;0,700;1,700&family=Fredoka:wght@600&display=swap">
<style>
  :root {
    --page: #ffffff;
    --van-body: #1f2527;
    --teal: #8cc3cc;
    --cream: #e9e6dc;
    --ink: #1f2527;
    --white: #f4f4f0;
  }
  html, body {
    margin: 0;
    padding: 0;
    width: 1200px;
    height: 1200px;
    overflow: hidden;
    background: var(--page);
  }
  .canvas {
    position: relative;
    width: 1200px;
    height: 1200px;
  }
  .side-panel {
    position: absolute;
    left: 0;
    top: 0;
  }
  .brand-mark {
    position: absolute;
    left: 560px;
    top: 440px;
    width: 130px;
    height: 130px;
    border-radius: 50%;
    border: 10px solid var(--teal);
    box-sizing: border-box;
  }
  .brand-name {
    position: absolute;
    left: 735px;
    top: 418px;
    margin: 0;
    font-family: "Poppins", sans-serif;
    font-weight: 700;
    font-size: 80px;
    line-height: 1;
    color: var(--teal);
    letter-spacing: 1px;
  }
  .tagline {
    position: absolute;
    left: 742px;
    top: 516px;
    margin: 0;
    font-family: "Poppins", sans-serif;
    font-weight: 700;
    font-size: 24px;
    line-height: 1;
    letter-spacing: 3px;
    color: var(--white);
    transform: rotate(-7deg);
    transform-origin: left center;
  }
  .contact {
    position: absolute;
    left: 262px;
    top: 600px;
    width: 230px;
    text-align: center;
    font-family: "Poppins", sans-serif;
  }
  .contact__phone {
    margin: 0;
    font-weight: 700;
    font-size: 23px;
    color: var(--teal);
  }
  .contact__web {
    margin: 2px 0 8px;
    font-style: italic;
    font-weight: 700;
    font-size: 17px;
    color: var(--white);
  }
  .social-list {
    display: flex;
    justify-content: center;
    gap: 6px;
    margin: 0;
    padding: 0;
    list-style: none;
  }
  .social-list li {
    width: 16px;
    height: 16px;
    border-radius: 50%;
    background: var(--white);
  }
  .services {
    position: absolute;
    left: 772px;
    top: 626px;
    display: grid;
    grid-template-columns: auto auto;
    column-gap: 12px;
    row-gap: 0;
    margin: 0;
    padding: 0;
    list-style: none;
    font-family: "Fredoka", sans-serif;
    font-weight: 600;
    font-size: 16px;
    line-height: 1.2;
    color: var(--ink);
    transform: rotate(-6deg);
    transform-origin: left top;
  }
  .services li::before {
    content: "";
    display: inline-block;
    width: 9px;
    height: 5px;
    margin: 0 5px 4px 1px;
    border-left: 2px solid var(--ink);
    border-bottom: 2px solid var(--ink);
    transform: rotate(-45deg);
  }
</style>
</head>
<body>
<main class="canvas">
  <svg class="side-panel" width="1200" height="1200" viewBox="0 0 1200 1200">
    <defs>
      <clipPath id="panel-clip">
        <rect x="60" y="390" width="1080" height="370" rx="40"/>
      </clipPath>
      <linearGradient id="circuit-tone" x1="0" y1="0" x2="1" y2="0">
        <stop offset="0" stop-color="#8cc3cc" stop-opacity="0"/>
        <stop offset="1" stop-color="#8cc3cc" stop-opacity="0.35"/>
      </linearGradient>
    </defs>
    <rect class="panel-body" x="60" y="390" width="1080" height="370" rx="40" fill="var(--van-body)"/>
    <g clip-path="url(#panel-clip)">
      <polygon class="top-stripe" points="700,390 1140,390 1140,404 712,404" fill="var(--teal)"/>
      <polygon class="light-band" points="600,760 690,760 752,616 1140,575 1140,553 712,598" fill="var(--cream)"/>
      <polygon class="service-band" points="700,760 1140,760 1140,583 758,623" fill="var(--teal)"/>
      <rect class="circuit-trace" x="330" y="695" width="250" height="55" fill="url(#circuit-tone)" role="img" aria-label="Decorative circuit board trace pattern"/>
    </g>
  </svg>

  <div class="brand-mark"></div>
  <h1 class="brand-name">KYNETRA</h1>
  <p class="tagline">GET CONNECTED</p>

  <div class="contact">
    <p class="contact__phone">+353 80 555 0142</p>
    <p class="contact__web">www.kynetra.ie</p>
    <ul class="social-list" aria-label="Social channels">
      <li aria-label="Lunemark"></li>
      <li aria-label="Quellorix"></li>
      <li aria-label="Bravitel"></li>
      <li aria-label="Marquine"></li>
      <li aria-label="Dovlette"></li>
    </ul>
  </div>

  <ul class="services">
    <li>Electrical</li>
    <li>EV Chargers</li>
    <li>Access Control</li>
    <li>Fire Protection</li>
    <li>Home Automation</li>
    <li>Intruder Alarms &amp; CCTV</li>
    <li>Fire Alarms</li>
  </ul>
</main>
</body>
</html>
```